Looking for something sharp classy and with an edge for an advanced civil construction business
Something that says professional
nothing too DARK

Target Market(s)

mining companies council civil contractors concrete works

Industry/Entity Type

Construction

Contact Information for Business Card

Ridgeline Civil Constructions
ridgelinecivilconstruction@mailtrove.net
Rewi Ashdown
0412758391

Font styles to use
Serif
Sans Serif

Colors
0455a3
0592cd
85cae6
000000
919191

Requirements
Must have
• On the back of the card must have
down the bottom small print email logo phone number

Should not have
• follow us on facebook
Ridgeline Civil Constructions

follow us on instagram
RIDGELINECIVILCONSTRUCTIONS

```html
<!DOCTYPE html>
<html lang="en">
<head>
<meta charset="utf-8">
<title>Ridgeline Civil Constructions — Business Card</title>
<link rel="stylesheet" href="https://fonts.googleapis.com/css2?family=Ubuntu:wght@300;400;500;700&display=swap">
<style>
  :root {
    --blue-deep: #0455a3;
    --blue: #0592cd;
    --sky: #85cae6;
    --black: #000000;
    --charcoal: #1c1f24;
    --grey: #919191;
    --white: #ffffff;
    --stage: #ecedef;
  }
  * { box-sizing: border-box; margin: 0; padding: 0; }
  html, body { width: 1120px; height: 1200px; overflow: hidden; }
  body {
    position: relative;
    background: var(--stage);
    font-family: "Ubuntu", Arial, sans-serif;
  }

  .presentation { position: absolute; left: 0; top: 0; width: 1120px; height: 852px; }

  .card {
    position: absolute;
    width: 490px;
    height: 280px;
    overflow: hidden;
    box-shadow: 0 14px 30px rgba(0,0,0,0.22);
  }
  .card--front {
    left: 50px; top: 250px;
    background: linear-gradient(160deg, #2a2e35 0%, var(--charcoal) 45%, var(--black) 100%);
  }
  .card--back { left: 580px; top: 300px; background: var(--white); }

  .wordmark {
    position: absolute;
    left: 0; right: 0;
    text-align: center;
    font-weight: 500;
    line-height: 1;
  }
  .wordmark__name { display: block; letter-spacing: 1px; }
  .wordmark__sub { display: block; letter-spacing: 2px; margin-top: 8px; }

  .card--front .wordmark { top: 84px; color: var(--blue); }
  .card--front .wordmark__name { font-size: 52px; }
  .card--front .wordmark__sub { font-size: 15px; color: var(--sky); }

  .front-footer {
    position: absolute;
    left: 0; right: 0; bottom: 0;
    height: 40px;
    display: flex;
    align-items: center;
    justify-content: center;
    gap: 26px;
    background: linear-gradient(90deg, var(--blue-deep), var(--blue));
    border-top: 3px solid var(--sky);
    color: var(--white);
    font-size: 11px;
    letter-spacing: 0.3px;
  }
  .front-footer span { display: flex; align-items: center; gap: 6px; }
  .front-footer svg { width: 11px; height: 11px; }

  .card--back .wordmark { top: 48px; color: var(--blue-deep); }
  .card--back .wordmark__name { font-size: 40px; }
  .card--back .wordmark__sub { font-size: 12px; }

  .card__band { position: absolute; left: 0; top: 0; width: 490px; height: 280px; }

  .holder { position: absolute; left: 36px; top: 200px; color: var(--white); }
  .holder__name { font-size: 19px; font-weight: 700; }
  .holder__role { font-size: 10px; letter-spacing: 1px; margin-top: 4px; text-transform: uppercase; }

  .contacts { position: absolute; right: 22px; top: 150px; list-style: none; color: var(--white); font-size: 10.5px; }
  .contacts li { display: flex; align-items: center; gap: 7px; margin-bottom: 6px; }
  .contacts svg { width: 11px; height: 11px; }

  .caption { position: absolute; left: 40px; top: 788px; display: flex; align-items: baseline; gap: 14px; }
  .caption__mark { color: var(--white); font-size: 15px; font-weight: 500; letter-spacing: 1px; background: #555; padding: 2px 6px; }
  .caption__label { color: #555; font-size: 19px; font-style: italic; font-weight: 300; }

  .panel { position: absolute; top: 852px; width: 560px; height: 348px; }
  .panel--dark { left: 0; background: var(--black); }
  .panel--light { left: 560px; background: var(--white); }
  .panel .wordmark { top: 136px; }
  .panel .wordmark__name { font-size: 48px; }
  .panel .wordmark__sub { font-size: 14px; }
  .panel--dark .wordmark { color: var(--blue); }
  .panel--light .wordmark { color: var(--blue-deep); }
</style>
</head>
<body>
  <section class="presentation">
    <article class="card card--front">
      <div class="wordmark">
        <span class="wordmark__name">RIDGELINE</span>
        <span class="wordmark__sub">CIVIL CONSTRUCTIONS</span>
      </div>
      <footer class="front-footer">
        <span>
          <svg viewBox="0 0 12 12" aria-hidden="true"><rect x="0.5" y="2" width="11" height="8" fill="#fff"/><polyline points="0.5,2 6,7 11.5,2" fill="none" stroke="#0455a3"/></svg>
          ridgelinecivilconstruction@mailtrove.net
        </span>
        <span>
          <svg viewBox="0 0 12 12" aria-hidden="true"><rect x="3" y="0.5" width="6" height="11" rx="1" fill="none" stroke="#fff"/><circle cx="6" cy="9.5" r="0.8" fill="#fff"/></svg>
          0412 758 391
        </span>
      </footer>
    </article>

    <article class="card card--back">
      <svg class="card__band" viewBox="0 0 490 280" aria-hidden="true">
        <defs>
          <linearGradient id="bandFill" x1="0" y1="0" x2="1" y2="0">
            <stop offset="0" stop-color="#0455a3"/>
            <stop offset="1" stop-color="#0592cd"/>
          </linearGradient>
        </defs>
        <polygon points="0,190 490,130 490,280 0,280" fill="url(#bandFill)"/>
        <polygon points="0,183 490,123 490,127 0,187" fill="#85cae6"/>
      </svg>
      <div class="wordmark">
        <span class="wordmark__name">RIDGELINE</span>
        <span class="wordmark__sub">CIVIL CONSTRUCTIONS</span>
      </div>
      <div class="holder">
        <p class="holder__name">Rewi Ashdown</p>
        <p class="holder__role">Manager</p>
      </div>
      <ul class="contacts">
        <li>
          <svg viewBox="0 0 12 12" aria-hidden="true"><rect x="3" y="0.5" width="6" height="11" rx="1" fill="none" stroke="#fff"/><circle cx="6" cy="9.5" r="0.8" fill="#fff"/></svg>
          0412 758 391
        </li>
        <li>
          <svg viewBox="0 0 12 12" aria-hidden="true"><rect x="0.5" y="2" width="11" height="8" fill="#fff"/><polyline points="0.5,2 6,7 11.5,2" fill="none" stroke="#0455a3"/></svg>
          rashdown@mailtrove.net
        </li>
        <li>
          <svg viewBox="0 0 12 12" aria-hidden="true"><circle cx="6" cy="6" r="5.5" fill="#fff"/><ellipse cx="6" cy="6" rx="2.3" ry="5.2" fill="none" stroke="#0592cd" stroke-width="0.8"/><line x1="0.5" y1="6" x2="11.5" y2="6" stroke="#0592cd" stroke-width="0.8"/></svg>
          www.ridgelinecivil.net
        </li>
      </ul>
    </article>

    <div class="caption">
      <span class="caption__mark">RIDGELINE</span>
      <span class="caption__label">Business Card*</span>
    </div>
  </section>

  <section class="panel panel--dark">
    <div class="wordmark">
      <span class="wordmark__name">RIDGELINE</span>
      <span class="wordmark__sub">CIVIL CONSTRUCTIONS</span>
    </div>
  </section>
  <section class="panel panel--light">
    <div class="wordmark">
      <span class="wordmark__name">RIDGELINE</span>
      <span class="wordmark__sub">CIVIL CONSTRUCTIONS</span>
    </div>
  </section>
</body>
</html>
```